Blue Heron Journeys

We are a predominantly online travel agency with high-end (first/business class) clients. I'm looking to either have our existing logo revamped or a new logo created with business card layout. I prefer to work with existing logo if possible so it remains familiar with existing clientele. I have uploaded a yellow business card layout showing icons on one side of the card. I would like to keep my existing colours, not yellow. could the company name/tag line go over the icons?
Contact Information for Business Card
Colleen Fairbank
Director
(G.T.L.C. 07815364)
(Quorvanel Pty. Ltd) ABN 61 507 314 829
512/48 Tillbrook Street
Calder Heights | NSW 2468 | Australia
www.blueheronjourneys-example.com.au
m: + 61 (0) 491 738 052
t: + 61 (0) 2 9175 3816
e: colleen@blueheronjourneys-example.com.au

```html
<!DOCTYPE html>
<html lang="en">
<head>
<meta charset="utf-8">
<title>Blue Heron Journeys – Business Card</title>
<link rel="stylesheet" href="https://fonts.googleapis.com/css2?family=Montserrat:wght@400;700&display=swap">
<style>
  :root {
    --backdrop: #474747;
    --peach: #f9c995;
    --peach-light: #fbd6ad;
    --card-white: #ffffff;
    --ink: #111111;
    --text-grey: #3f3f3f;
    --muted-grey: #8a8a8a;
  }
  * { margin: 0; padding: 0; box-sizing: border-box; }
  html, body {
    width: 1200px; height: 1200px; overflow: hidden;
    background: var(--backdrop);
  }
  .sheet {
    position: relative; width: 1200px; height: 1200px;
    display: flex; flex-direction: column; align-items: center; justify-content: center;
    gap: 60px;
  }
  .card {
    position: relative; width: 720px; height: 440px;
    box-shadow: 0 10px 30px rgba(0,0,0,0.35);
    overflow: hidden;
    font-family: "Montserrat", sans-serif;
  }

  /* Front */
  .card-front { background: var(--peach); }
  .travel-pattern {
    position: absolute; inset: 0;
    background: radial-gradient(circle at 50% 50%, var(--peach-light), var(--peach) 70%);
  }
  .brand {
    position: absolute; left: 0; right: 0; top: 168px;
    text-align: center;
    color: var(--ink);
  }
  .brand-name { font-weight: 700; font-size: 46px; line-height: 1; }
  .brand-tagline {
    font-weight: 400; font-size: 24px; line-height: 1;
    margin-top: 26px; color: var(--text-grey);
  }

  /* Back */
  .card-back {
    background: var(--card-white);
    color: var(--text-grey);
    padding: 52px 0 0 72px;
  }
  .holder-name { font-weight: 700; font-size: 19px; color: var(--ink); }
  .holder-role { font-size: 17px; color: var(--muted-grey); margin-top: 2px; }
  .contact-list { list-style: none; margin-top: 28px; }
  .contact-row { display: flex; align-items: flex-start; margin-bottom: 18px; }
  .contact-icon {
    width: 48px; height: 42px; border-radius: 6px;
    background: var(--peach);
    display: flex; align-items: center; justify-content: center;
    flex-shrink: 0;
  }
  .contact-icon svg { width: 22px; height: 22px; }
  .contact-text {
    margin-left: 32px; font-size: 17px; line-height: 1.35; padding-top: 2px;
  }
  .corner-tab {
    position: absolute; left: 0; bottom: 44px;
    width: 48px; height: 42px; border-radius: 0 6px 6px 0;
    background: var(--peach);
  }
</style>
</head>
<body>
<main class="sheet">

  <section class="card card-front" aria-label="Card front">
    <div class="travel-pattern" role="img" aria-label="Light line-icon pattern of travel motifs: planes, palms, bikes, cakes, cameras, cars, calendars and sun umbrellas"></div>
    <div class="brand">
      <div class="brand-name">Blue Heron Journeys</div>
      <div class="brand-tagline">travel at your own pace</div>
    </div>
  </section>

  <section class="card card-back" aria-label="Card back">
    <div class="holder">
      <div class="holder-name">Colleen Fairbank</div>
      <div class="holder-role">Director</div>
    </div>
    <ul class="contact-list">
      <li class="contact-row">
        <span class="contact-icon">
          <svg viewBox="0 0 24 24" fill="#fff"><path d="M6.6 10.8a15.1 15.1 0 0 0 6.6 6.6l2.2-2.2c.3-.3.7-.4 1-.2 1.1.4 2.3.6 3.6.6.6 0 1 .4 1 1V20c0 .6-.4 1-1 1A17 17 0 0 1 3 4c0-.6.4-1 1-1h3.5c.6 0 1 .4 1 1 0 1.3.2 2.5.6 3.6.1.3 0 .7-.2 1z"/></svg>
        </span>
        <span class="contact-text">+ 61 (0) 491 738 052<br>+ 61 (0) 2 9175 3816</span>
      </li>
      <li class="contact-row">
        <span class="contact-icon">
          <svg viewBox="0 0 24 24" fill="none" stroke="#fff" stroke-width="2"><circle cx="12" cy="12" r="9"/><path d="M3 12h18M12 3c3 3 3 15 0 18M12 3c-3 3-3 15 0 18"/></svg>
        </span>
        <span class="contact-text">www.blueheronjourneys-example.com.au<br>colleen@blueheronjourneys-example.com.au</span>
      </li>
      <li class="contact-row">
        <span class="contact-icon">
          <svg viewBox="0 0 24 24" fill="#fff"><path d="M12 3 2 12h3v8h5v-5h4v5h5v-8h3z"/></svg>
        </span>
        <span class="contact-text">(G.T.L.C. 07815364)<br>(Quorvanel Pty. Ltd) ABN 61 507 314 829<br>512/48 Tillbrook Street<br>Calder Heights | NSW 2468 | Australia</span>
      </li>
    </ul>
    <div class="corner-tab"></div>
  </section>

</main>
</body>
</html>
```